HARLOWE FREIGHT & PLANT HIRE NEEDS A FLYER

WE NEED A FLYER FOR OUR COMPANY <br/>WE SPECIALISE IN ROAD BUILDING AND MAINTENANCE, GENERAL EARTHWORK DAM REPAIRS & DESILTING, FENCE CLEARING, FIRE BREAKS, GRAVEL SOURCE AND DELIVERY GENERAL FREIGHT STEEL HAY LICK AND MCHINERY. <br/><br/>I HAVE UPLOAD A FILE THAT I LIKE AND WOULD LIKE SOMETHING THE SAME IF POSSIBLE. AND LOGO TO GO WITH IT.

```html
<!DOCTYPE html>
<html lang="en">
<head>
<meta charset="utf-8">
<title>Harlowe Freight &amp; Plant Hire – Flyer</title>
<link rel="stylesheet" href="https://fonts.googleapis.com/css2?family=Oswald:wght@300;500;600&family=Rubik:wght@500;600;700&family=Roboto+Slab:wght@500;700;800&display=swap">
<style>
  :root{
    --stage:#2b2b2b;
    --black:#0c0c0c;
    --charcoal:#3a3a3c;
    --gold:#f5b300;
    --gold-deep:#e49a0c;
    --amber:#f7a51c;
    --ink:#2a2a2a;
    --white:#ffffff;
    --paper:#f7f7f9;
  }
  *{box-sizing:border-box;margin:0;padding:0}
  html,body{width:1200px;height:1200px;overflow:hidden;background:var(--stage)}
  .flyer{position:absolute;left:113px;top:245px;width:967px;height:731px;background:var(--paper);overflow:hidden;box-shadow:0 6px 18px rgba(0,0,0,.45);font-family:"Rubik",sans-serif}
  .header{position:absolute;left:0;top:0;width:967px;height:184px;background:var(--black)}
  .brand{position:absolute;left:92px;top:48px;width:310px;text-align:center;font-family:"Oswald",sans-serif;font-weight:600;color:var(--gold);line-height:1}
  .brand .name{display:block;font-size:58px;letter-spacing:1px}
  .brand .trade{display:block;font-size:30px;margin-top:4px}
  .brand .suffix{display:block;font-size:19px;margin-top:6px;letter-spacing:1px}
  .tagline{position:absolute;left:425px;top:60px;width:520px;text-align:center;font-family:"Oswald",sans-serif;font-weight:300;font-size:38px;line-height:48px;color:var(--white);letter-spacing:-.5px;white-space:nowrap}
  .tagline strong{font-weight:500;color:var(--amber)}
  .hazard{position:absolute;left:0;width:967px;height:14px;background:var(--black);padding:2px 0}
  .hazard::before{content:"";display:block;height:10px;background:repeating-linear-gradient(110deg,var(--gold) 0 8px,var(--black) 8px 13px)}
  .hazard--top{top:183px}
  .hazard--bottom{top:595px}
  .photo{position:absolute}
  .photo--grader-blade{left:0;top:197px;width:383px;height:302px;background:linear-gradient(160deg,#c7b497 0%,#a8895a 45%,#6b6a64 80%,#3e4a5c 100%)}
  .photo--grader{left:390px;top:197px;width:225px;height:170px;background:linear-gradient(180deg,#9cc3e6 0%,#cfe0ee 50%,#8d8a7a 80%,#5b5b58 100%)}
  .photo--water-truck{left:390px;top:377px;width:225px;height:122px;background:linear-gradient(180deg,#d8dbe0 0%,#aeb3ba 55%,#6e7279 100%)}
  .specialties{position:absolute;left:615px;top:197px;width:352px;height:398px;background:linear-gradient(180deg,var(--gold) 0%,var(--gold) 45%,var(--gold-deep) 100%);padding:18px 0 0 12px}
  .specialties h2{font-size:20px;font-weight:600;color:var(--ink);margin-bottom:6px}
  .specialties ul{list-style:none}
  .specialties li{display:flex;align-items:center;height:26px;font-size:18px;font-weight:600;color:var(--ink)}
  .specialties li svg{width:18px;height:18px;margin:0 9px 0 4px;flex:none}
  .photo--forklift{left:762px;top:440px;width:190px;height:232px;border-radius:6px;background:linear-gradient(180deg,rgba(40,40,40,.55) 0%,rgba(230,200,30,.85) 55%,rgba(30,30,30,.7) 100%)}
  .machinery{position:absolute;left:0;top:499px;width:615px;height:96px;background:var(--charcoal)}
  .machinery h3{position:absolute;left:0;top:12px;width:328px;height:25px;background:var(--gold);font-size:19px;font-weight:600;color:var(--ink);padding-left:38px;line-height:25px;letter-spacing:-.3px}
  .machinery p{position:absolute;left:40px;font-size:17px;font-weight:600;color:var(--white);letter-spacing:-.2px;white-space:nowrap}
  .machinery p:nth-of-type(1){top:42px}
  .machinery p:nth-of-type(2){top:64px}
  .sep{display:inline-block;width:4px;height:4px;background:var(--gold);margin:0 4px;vertical-align:middle}
  .contact-label{position:absolute;left:40px;top:620px;font-family:"Roboto Slab",serif;color:var(--ink);line-height:1;white-space:nowrap}
  .contact-label .lead{display:block;font-size:30px;font-weight:500}
  .contact-label .people{display:block;font-size:28px;font-weight:700;margin-top:2px}
  .phone{position:absolute;left:383px;top:626px;display:flex;align-items:center}
  .phone svg{width:40px;height:44px}
  .phone span{margin-left:12px;font-family:"Roboto Slab",serif;font-weight:800;font-size:44px;color:var(--amber);-webkit-text-stroke:2px var(--ink);letter-spacing:-1px}
  .email{position:absolute;left:387px;top:674px;display:flex;align-items:center}
  .email svg{width:32px;height:22px}
  .email span{margin-left:14px;font-family:"Roboto Slab",serif;font-weight:700;font-size:22px;color:var(--ink);white-space:nowrap}
</style>
</head>
<body>
<main class="flyer">
  <header class="header">
    <div class="brand"><span class="name">HARLOWE</span><span class="trade">FREIGHT &amp; PLANT HIRE</span><span class="suffix">PTY LTD</span></div>
    <h1 class="tagline">FOR ALL YOUR <strong>FREIGHT</strong> &amp; <strong>PLANT</strong><br><strong>HIRE</strong> NEEDS!</h1>
  </header>
  <div class="hazard hazard--top"></div>

  <div class="photo photo--grader-blade" role="img" aria-label="Close-up of a yellow grader blade on a dirt site under a cloudy sky"></div>
  <div class="photo photo--grader" role="img" aria-label="Yellow road grader on a sealed road"></div>
  <div class="photo photo--water-truck" role="img" aria-label="Water truck spraying a road"></div>

  <section class="specialties">
    <h2>Specialising In :</h2>
    <ul>
      <li><svg viewBox="0 0 18 18"><rect x="1" y="3" width="13" height="13" fill="none" stroke="#2a2a2a" stroke-width="2"/><path d="M4 9l3.5 3.5L17 2" fill="none" stroke="#2a2a2a" stroke-width="2.4"/></svg>Road Building and Maintenance</li>
      <li><svg viewBox="0 0 18 18"><rect x="1" y="3" width="13" height="13" fill="none" stroke="#2a2a2a" stroke-width="2"/><path d="M4 9l3.5 3.5L17 2" fill="none" stroke="#2a2a2a" stroke-width="2.4"/></svg>General Earthworks</li>
      <li><svg viewBox="0 0 18 18"><rect x="1" y="3" width="13" height="13" fill="none" stroke="#2a2a2a" stroke-width="2"/><path d="M4 9l3.5 3.5L17 2" fill="none" stroke="#2a2a2a" stroke-width="2.4"/></svg>Dam Repairs &amp; Destiling</li>
      <li><svg viewBox="0 0 18 18"><rect x="1" y="3" width="13" height="13" fill="none" stroke="#2a2a2a" stroke-width="2"/><path d="M4 9l3.5 3.5L17 2" fill="none" stroke="#2a2a2a" stroke-width="2.4"/></svg>Fence Clearing</li>
      <li><svg viewBox="0 0 18 18"><rect x="1" y="3" width="13" height="13" fill="none" stroke="#2a2a2a" stroke-width="2"/><path d="M4 9l3.5 3.5L17 2" fill="none" stroke="#2a2a2a" stroke-width="2.4"/></svg>Fire Breaks</li>
      <li><svg viewBox="0 0 18 18"><rect x="1" y="3" width="13" height="13" fill="none" stroke="#2a2a2a" stroke-width="2"/><path d="M4 9l3.5 3.5L17 2" fill="none" stroke="#2a2a2a" stroke-width="2.4"/></svg>Gravel Source &amp; Delivery</li>
      <li><svg viewBox="0 0 18 18"><rect x="1" y="3" width="13" height="13" fill="none" stroke="#2a2a2a" stroke-width="2"/><path d="M4 9l3.5 3.5L17 2" fill="none" stroke="#2a2a2a" stroke-width="2.4"/></svg>General Freight</li>
      <li><svg viewBox="0 0 18 18"><rect x="1" y="3" width="13" height="13" fill="none" stroke="#2a2a2a" stroke-width="2"/><path d="M4 9l3.5 3.5L17 2" fill="none" stroke="#2a2a2a" stroke-width="2.4"/></svg>Steel</li>
      <li><svg viewBox="0 0 18 18"><rect x="1" y="3" width="13" height="13" fill="none" stroke="#2a2a2a" stroke-width="2"/><path d="M4 9l3.5 3.5L17 2" fill="none" stroke="#2a2a2a" stroke-width="2.4"/></svg>Lick</li>
      <li><svg viewBox="0 0 18 18"><rect x="1" y="3" width="13" height="13" fill="none" stroke="#2a2a2a" stroke-width="2"/><path d="M4 9l3.5 3.5L17 2" fill="none" stroke="#2a2a2a" stroke-width="2.4"/></svg>Hay</li>
      <li><svg viewBox="0 0 18 18"><rect x="1" y="3" width="13" height="13" fill="none" stroke="#2a2a2a" stroke-width="2"/><path d="M4 9l3.5 3.5L17 2" fill="none" stroke="#2a2a2a" stroke-width="2.4"/></svg>Machinery</li>
    </ul>
  </section>

  <section class="machinery">
    <h3>Current Machinery Available</h3>
    <p>Grader<i class="sep"></i>Load &amp; Stick<i class="sep"></i>Rack<i class="sep"></i>Rollers<i class="sep"></i>Dozers<i class="sep"></i>Water Trucks</p>
    <p>Prime Movers<i class="sep"></i>Forklift<i class="sep"></i>Skid Steer Loader<i class="sep"></i>Flat Top<i class="sep"></i>Drop Deck</p>
  </section>
  <div class="hazard hazard--bottom"></div>

  <div class="photo photo--forklift" role="img" aria-label="Yellow and black electric forklift"></div>

  <footer>
    <div class="contact-label"><span class="lead">Contact</span><span class="people">Daniel &amp; Megan Ashcroft</span></div>
    <div class="phone">
      <svg viewBox="0 0 40 44"><rect x="0" y="0" width="40" height="44" rx="8" fill="#0c0c0c"/><path d="M15 9c-3 1-5 3-5 6 0 8 7 18 15 21 3 1 5 0 7-2l-4-6-4 2c-3-2-6-7-7-10l3-3-3-8z" fill="none" stroke="#fff" stroke-width="2.4" stroke-linejoin="round"/></svg>
      <span>0400123987</span>
    </div>
    <div class="email">
      <svg viewBox="0 0 32 22"><rect x="1" y="1" width="30" height="20" fill="none" stroke="#2a2a2a" stroke-width="2"/><path d="M1 1l15 12L31 1M1 21l11-10M31 21L20 11" fill="none" stroke="#2a2a2a" stroke-width="2"/></svg>
      <span>megan.ashcroft@mailbox.com</span>
    </div>
  </footer>
</main>
</body>
</html>
```